Business card design for new software start-up

This design is for a double-sided, colour business card. The requirements are as follows:
PREVIEW IMAGES:
The preview images of the card should be shown on a white background (i.e. no wood veneers etc).
The preview images for the front and back of the card should be presented top to bottom without overlapping.
OVERALL DESIGN:
Clean, crisp and simple
LOGO COLOURS:
Green - CMYK 50C 100Y (PMS 376)
Grey - CMYK 80K
CARD SIZES:
Trim Size (Card Size) 90mm x 55mm
Margin Size: 80mm x 45mm
Bleed Size: 96mm x 61mm (i.e. 3mm bleed)
The corners of the card should be SQUARE and NOT ROUNDED.
CARD ORIENTATION:
Landscape (i.e. horizontal).
FRONT OF CARD:
- White background
- Lumatrek logo with tag line
- VentoHub logo scaled to a width of 1.25 inches and not as prominent as the Lumatrek logo
- The VentoHub logo should be placed on a plain background, not overlapping any background images
- Details:
Corwin Aldape
Founder and Chief Software Architect
Lumatrek Pty Ltd
Suite 2407, 15-19 Marlow St
Sydney NSW 2000
Australia
M: +61 (0) 555 0142
E: corwin.aldape@lumatrek-example.com
www.lumatrek-example.com
BACK OF CARD
- Lumatrek logo without tag line
- www.lumatrek-example.com
The back of the card should reflect the concept of being ahead of the curve in a simple or abstract way. Some possible ideas are as follows but other creative suggestions will also be considered:
1) A bell curve taking up the entire area, with the Lumatrek logo on the right, near a position ahead of the curve;
2) A graphical, curved arrow with the Lumatrek logo near the top of the arrow;
3) An abstract curve with the Lumatrek logo near the top of the curve.
At least a portion of the background colour should consist of the logo's green colour using colour code CMYK 50C 100Y (PMS 376). For designs that place the logo over a green background, the colour of the dot over the first "i" may be changed so that it is still visible.
SOURCE FILES
Must be in AI format with 2 versions:
(1) With editable texts/fonts to allow for name and address changes in future;
(2) With all text converted to vectors/paths
PRINT FILES
Must be delivered in PDF, TIFF, JPG, EPS and PSD formats
Images should be 300 DPI
Updates
Revision to design for back of card:
The back of the card should also include the web address: www.lumatrek-example.com
At least a portion of the background colour should consist of the logo's green colour. For designs that place the logo over a green background, the colour of the dot over the first "i" may be changed so that it is still visible.
Additional information:
1) The VentoHub logo should be placed on a plain background, not overlapping any background images;
2) The orientation of the card should be landscape (i.e. horizontal).

```html
<!DOCTYPE html>
<html lang="en">
<head>
<meta charset="utf-8">
<title>Lumatrek business card</title>
<link rel="stylesheet" href="https://fonts.googleapis.com/css2?family=Arimo:wght@400;700&display=swap">
<style>
  :root {
    --brand-green: #8cc63f;
    --brand-green-light: #b5db7c;
    --brand-grey: #58595b;
    --ink: #231f20;
    --white: #ffffff;
    --badge-blue: #1d3f7a;
    --backdrop: #f4f4f2;
  }
  * { box-sizing: border-box; margin: 0; padding: 0; }
  html, body { width: 1200px; height: 939px; overflow: hidden; }
  body {
    position: relative;
    background: var(--backdrop);
    font-family: "Arimo", Arial, sans-serif;
    color: var(--ink);
  }
  .card {
    position: absolute; left: 250px; width: 700px; height: 428px;
    overflow: hidden; box-shadow: 0 2px 10px rgba(0,0,0,0.18);
  }

  /* Front of card */
  .card-front { top: 20px; background: var(--white); }
  .front-swoosh { position: absolute; inset: 0; }
  .header-band {
    position: absolute; left: 0; top: 0; width: 700px; height: 126px;
    background: var(--brand-grey);
  }
  .header-band .wordmark {
    position: absolute; left: 42px; top: 30px;
    font-size: 62px; font-weight: 700; letter-spacing: -1.5px;
    color: var(--white); line-height: 1;
  }
  .header-band .divider {
    position: absolute; left: 376px; top: 34px; width: 2px; height: 60px;
    background: var(--white);
  }
  .header-band .tagline {
    position: absolute; left: 392px; top: 36px;
    font-size: 17px; font-weight: 700; line-height: 1.08;
    color: var(--white); text-transform: uppercase;
  }
  .address {
    position: absolute; left: 42px; top: 156px;
    font-size: 20px; line-height: 28px; white-space: nowrap;
  }
  .contact { margin-top: 8px; }
  .label { color: var(--brand-green); font-weight: 700; }
  .web-front { margin-top: 6px; color: var(--brand-green); font-weight: 700; }
  .person {
    position: absolute; left: 398px; top: 156px;
    font-size: 20px; line-height: 28px; white-space: nowrap;
  }
  .person .name { font-weight: 700; text-transform: uppercase; }
  .partner-badge {
    position: absolute; left: 492px; top: 292px; width: 158px; height: 68px;
    background: var(--badge-blue); border-radius: 3px;
  }

  /* Back of card */
  .card-back { top: 492px; background: var(--brand-green); }
  .card-back .wordmark {
    position: absolute; left: 186px; top: 112px;
    font-size: 100px; font-weight: 700; letter-spacing: -3px;
    color: var(--brand-grey); line-height: 1; white-space: nowrap;
  }
  .card-back .web {
    position: absolute; right: 59px; top: 246px;
    font-size: 20px; font-weight: 700; color: var(--white); white-space: nowrap;
  }
</style>
</head>
<body>
  <section class="card card-front" aria-label="Front of card">
    <svg class="front-swoosh" width="700" height="428" viewBox="0 0 700 428" aria-hidden="true">
      <path d="M150 428 C380 410 590 320 700 210 L700 236 C600 338 410 420 240 428 Z" fill="var(--brand-green-light)"/>
      <path d="M250 428 C440 414 610 336 700 248 L700 428 Z" fill="var(--brand-green)"/>
    </svg>

    <header class="header-band">
      <div class="wordmark">Lumatrek</div>
      <div class="divider"></div>
      <div class="tagline">Software<br>ahead of<br>the curve</div>
    </header>

    <div class="address">
      <p>Lumatrek Pty Ltd</p>
      <p>Suite 2407, 15-19 Marlow St</p>
      <p>Sydney NSW 2000</p>
      <p>Australia</p>
      <p class="contact"><span class="label">M:</span> +61 (0) 555 0142</p>
      <p><span class="label">E:</span> corwin.aldape@lumatrek-example.com</p>
      <p class="web-front">www.lumatrek-example.com</p>
    </div>

    <div class="person">
      <p class="name">Corwin Aldape</p>
      <p>Founder and</p>
      <p>Chief Software Architect</p>
    </div>

    <div class="partner-badge" role="img" aria-label="VentoHub partner badge"></div>
  </section>

  <section class="card card-back" aria-label="Back of card">
    <div class="wordmark">Lumatrek</div>
    <div class="web">www.lumatrek-example.com</div>
  </section>
</body>
</html>
```